kestrel home systems HERS

Looking for business card design that represents our company. we are kestrel home systems and we dedicate our skills of home energy efficiency to our customer by providing energy solution to their energy problems.
HVAC
SOLAR
INSULLATION
LIGHTING
DUCT TESTING
HERS RATING.

```html
<!DOCTYPE html>
<html lang="en">
<head>
<meta charset="utf-8">
<title>Kestrel Home Systems – Business Card</title>
<link rel="stylesheet" href="https://fonts.googleapis.com/css2?family=Roboto:wght@300;400;700&display=swap">
<style>
  :root {
    --backdrop: #e9e6e1;
    --card: #050505;
    --green: #7cc242;
    --leaf: #3d5a25;
    --navy: #1d4a66;
    --white: #f4f4f4;
    --muted: #c9c9c9;
  }
  * { margin: 0; padding: 0; box-sizing: border-box; }
  html, body { width: 1200px; height: 891px; overflow: hidden; }
  body {
    background: var(--backdrop);
    font-family: "Roboto", Arial, sans-serif;
    position: relative;
  }
  .card {
    position: absolute;
    width: 500px;
    height: 286px;
    background: var(--card);
    border-radius: 4px;
    box-shadow: 0 10px 30px rgba(0,0,0,.25);
    overflow: hidden;
  }
  .card--contact { left: 70px; top: 302px; }
  .card--brand { left: 630px; top: 302px; }

  /* contact side */
  .person { position: absolute; left: 40px; top: 38px; z-index: 1; }
  .person__name {
    font-size: 28px; font-weight: 400; color: var(--white);
    letter-spacing: .5px; text-transform: uppercase;
  }
  .person__name strong { color: var(--green); font-weight: 700; }
  .person__role {
    font-size: 13px; font-weight: 300; color: var(--muted);
    letter-spacing: 1px; text-transform: uppercase; margin-top: 2px;
  }
  .person__rule { width: 175px; height: 2px; background: var(--green); margin-top: 12px; }
  .contact-list { list-style: none; margin-top: 14px; }
  .contact-list li {
    display: flex; align-items: flex-start; gap: 12px;
    font-size: 13px; font-weight: 300; color: var(--white);
    line-height: 16px; margin-bottom: 8px;
  }
  .contact-list svg { width: 12px; height: 12px; flex: none; margin-top: 2px; fill: var(--green); }
  .sun-art {
    position: absolute; right: 0; bottom: 0;
    width: 215px; height: 160px;
    background: linear-gradient(135deg, var(--leaf) 0%, var(--navy) 100%);
    opacity: .85;
  }

  /* brand side */
  .brand {
    position: absolute; left: 0; right: 0; top: 104px;
    display: flex; justify-content: center; align-items: center; gap: 12px;
  }
  .brand__dot { width: 22px; height: 22px; border-radius: 50%; background: var(--green); }
  .brand__name {
    font-size: 30px; font-weight: 700; color: var(--green);
    text-transform: uppercase; letter-spacing: 1px;
  }
  .web {
    position: absolute; left: 0; right: 0; top: 212px; text-align: center;
    font-size: 13px; color: var(--white); letter-spacing: 2px;
  }
</style>
</head>
<body>
  <section class="card card--contact">
    <div class="person">
      <h1 class="person__name"><strong>Dana</strong> Whitfield</h1>
      <p class="person__role">Creative Designer</p>
      <div class="person__rule"></div>
      <ul class="contact-list">
        <li><svg viewBox="0 0 12 12"><path d="M2 1l2 0 1 3-1.5 1a7 7 0 0 0 3.5 3.5L8 7l3 1v2c0 1-1 1-1 1A9 9 0 0 1 1 2s0-1 1-1z"/></svg>+000 12345 6789</li>
        <li><svg viewBox="0 0 12 12"><path d="M11 1L1 5l4 2 2 4z"/></svg>urname@email.com</li>
        <li><svg viewBox="0 0 12 12"><path d="M6 0a4 4 0 0 0-4 4c0 3 4 8 4 8s4-5 4-8a4 4 0 0 0-4-4zm0 6a2 2 0 1 1 0-4 2 2 0 0 1 0 4z"/></svg>Street Address Here<br>Singapore, 2222</li>
        <li><svg viewBox="0 0 12 12"><circle cx="3" cy="6" r="2"/><circle cx="9" cy="2.5" r="2"/><circle cx="9" cy="9.5" r="2"/><path d="M3 6L9 2.5M3 6l6 3.5" stroke="#7cc242" stroke-width="1"/></svg>urwebsitename.com</li>
      </ul>
    </div>
    <div class="sun-art" role="img" aria-label="Large brand illustration of a sun with leaf-shaped rays"></div>
  </section>

  <section class="card card--brand">
    <div class="brand">
      <span class="brand__dot"></span>
      <span class="brand__name">Kestrel Home Systems</span>
    </div>
    <p class="web">www.kestrelhome.com</p>
  </section>
</body>
</html>
```